Window Decal Design

I have office windows that need a design incorporating from my logo. It should be semi transparent and offer enough privacy for meetings.

Size of the window is 450cm by 295cm

Colors
F0912C
F2A743
F7CA91
FBE8D2
FDF5EE

```html
<!DOCTYPE html>
<html lang="en">
<head>
<meta charset="utf-8">
<title>Solvista Holiday Rentals – Window Decal</title>
<link rel="stylesheet" href="https://fonts.googleapis.com/css2?family=Anton&family=Oswald:wght@700&family=Poppins:wght@600;700&display=swap">
<style>
  :root {
    --page-bg: #e2e2e2;
    --decal-bg: #ffffff;
    --ink-grey: #555558;
    --rule-grey: #8a8a8a;
    --mark-grey: #6a6a6c;
    --orange: #f0912c;
    --orange-deep: #e9821c;
    --orange-soft: #f2a743;
    --peach: #f7ca91;
    --cream: #fbe8d2;
    --shell: #fdf5ee;
  }
  * { margin: 0; padding: 0; box-sizing: border-box; }
  html, body {
    width: 800px;
    height: 1200px;
    overflow: hidden;
    background: var(--page-bg);
  }
  .canvas {
    position: relative;
    width: 800px;
    height: 1200px;
  }
  .decal {
    position: absolute;
    left: 20px;
    top: 351px;
    width: 760px;
    height: 497px;
    background: var(--decal-bg);
    box-shadow: 0 6px 22px rgba(0, 0, 0, 0.18);
    overflow: hidden;
  }
  .decal__pattern {
    position: absolute;
    inset: 0;
    background:
      radial-gradient(ellipse at 88% 12%, rgba(160,160,165,0.22), transparent 45%),
      radial-gradient(ellipse at 6% 18%, rgba(150,150,155,0.2), transparent 40%),
      radial-gradient(ellipse at 92% 88%, rgba(150,150,155,0.2), transparent 42%),
      radial-gradient(ellipse at 14% 88%, rgba(170,170,175,0.16), transparent 40%),
      linear-gradient(180deg, #fbfbfb, #f4f4f5);
  }
  .headline-luxury {
    position: absolute;
    left: 72px;
    top: 140px;
    font-family: "Oswald", "Arial Narrow", sans-serif;
    font-weight: 700;
    font-size: 60px;
    line-height: 1;
    letter-spacing: 0.5px;
    color: var(--ink-grey);
  }
  .brand {
    position: absolute;
    left: 310px;
    top: 146px;
    display: flex;
    align-items: center;
    gap: 10px;
  }
  .brand__dot {
    width: 40px;
    height: 40px;
    border-radius: 50%;
    background: var(--orange);
    flex: none;
  }
  .brand__name {
    font-family: "Poppins", sans-serif;
    font-weight: 700;
    color: var(--orange);
    line-height: 1;
  }
  .brand__name-main { display: block; font-size: 30px; letter-spacing: 0.5px; }
  .brand__name-sub { display: block; font-size: 13px; margin-top: 2px; letter-spacing: 0.3px; }
  .headline-apartments {
    position: absolute;
    left: 72px;
    top: 196px;
    font-family: "Anton", "Impact", sans-serif;
    font-size: 104px;
    line-height: 1;
    letter-spacing: -1px;
    color: var(--orange-deep);
  }
  .headline-villas {
    position: absolute;
    left: 272px;
    top: 292px;
    font-family: "Oswald", "Arial Narrow", sans-serif;
    font-weight: 700;
    font-size: 50px;
    line-height: 1;
    letter-spacing: 1px;
    color: var(--ink-grey);
  }
  .headline-rule {
    position: absolute;
    left: 76px;
    top: 339px;
    width: 186px;
    height: 1px;
    background: var(--rule-grey);
  }
  .feature-square {
    position: absolute;
    left: 590px;
    top: 208px;
    width: 124px;
    height: 124px;
    background: var(--mark-grey);
  }
  .web-address {
    position: absolute;
    left: 0;
    right: 0;
    top: 432px;
    padding-right: 10px;
    text-align: center;
    font-family: "Poppins", sans-serif;
    font-weight: 600;
    font-size: 14px;
    letter-spacing: 1.4px;
    color: var(--ink-grey);
  }
</style>
</head>
<body>
  <main class="canvas">
    <section class="decal">
      <div class="decal__pattern" role="img" aria-label="Faint grey hexagon network with dots and flowing fine-line waves in the corners"></div>

      <h1 class="headline">
        <span class="headline-luxury">LUXURY</span>
        <span class="headline-apartments">APARTMENTS</span>
        <span class="headline-villas">AND VILLAS</span>
      </h1>
      <div class="headline-rule"></div>

      <div class="brand">
        <span class="brand__dot"></span>
        <span class="brand__name">
          <span class="brand__name-main">SOLVISTA</span>
          <span class="brand__name-sub">HOLIDAY RENTALS</span>
        </span>
      </div>

      <div class="feature-square"></div>

      <p class="web-address">WWW.SOLVISTAHOLIDAYRENTALS.COM</p>
    </section>
  </main>
</body>
</html>
```